Website update for Harbor Broker Ledger & Payroll Services

Our website needs updating
www.harborbrokerledgers.com
Here are some of our latest print pieces to use as a guide?
I have also attached our graphic identity guide which includes the Pantone colors

Target Market(s)

Insurance Agencies

Industry/Entity Type

Accounting

Number of Pages Required

5+ page

```html
<!DOCTYPE html>
<html lang="en">
<head>
<meta charset="utf-8">
<title>Harbor Broker Ledger &amp; Payroll Services</title>
<link rel="stylesheet" href="https://fonts.googleapis.com/css2?family=Open+Sans:wght@400;600;700&display=swap">
<style>
:root{
  --teal:#17a398;
  --teal-dark:#128a80;
  --ink:#2b3a42;
  --text:#5a6770;
  --muted:#8a959c;
  --light:#f1f3f4;
  --footer:#2a2f34;
  --footer-deep:#1f2327;
  --white:#ffffff;
}
*{box-sizing:border-box;margin:0;padding:0}
html,body{width:1200px;height:2388px;overflow:hidden}
body{font-family:"Open Sans",Arial,sans-serif;color:var(--text);background:var(--white);position:relative}
.container{width:1080px;margin:0 auto;position:relative}

/* header */
.site-header{height:120px;position:relative}
.brand{position:absolute;left:60px;top:18px;display:flex;align-items:center;gap:12px}
.brand-mark{width:18px;height:18px;background:var(--teal)}
.brand-name{font-weight:700;font-size:17px;color:var(--ink);width:150px;line-height:1.2}
.tagline{position:absolute;left:260px;top:20px;font-size:17px;line-height:1.35;color:var(--ink);width:420px}
.main-nav{position:absolute;right:60px;top:84px;display:flex;background:var(--white)}
.main-nav a{display:block;padding:0 16px;height:36px;line-height:36px;font-size:11px;font-weight:600;color:var(--ink);text-decoration:none;letter-spacing:.3px}
.main-nav a.active{background:var(--teal);color:var(--white)}

/* hero */
.hero{position:relative;height:540px;background:linear-gradient(120deg,#e9eef1 0%,#cfd8de 45%,#8e9aa3 75%,#55616b 100%)}
.hero-photo{position:absolute;inset:0}
.hero-caption{position:absolute;left:170px;top:250px;width:420px;background:rgba(255,255,255,.82);padding:20px 24px;font-size:19px;line-height:1.5;color:var(--ink);font-weight:600}
.hero-arrows{position:absolute;left:596px;top:488px;display:flex;gap:6px}
.hero-arrows span{width:36px;height:36px;background:var(--teal);display:flex;align-items:center;justify-content:center}

/* need help */
.need-help{padding:120px 0 0;height:320px;position:relative}
.need-help h2{font-size:22px;color:var(--ink);font-weight:700;margin-bottom:18px}
.tick-list{list-style:none}
.tick-list li{font-size:12px;line-height:1.9;display:flex;align-items:center;gap:8px}
.tick-list li::before{content:"";width:7px;height:7px;border-radius:50%;background:var(--teal);flex:none}
.money-art{position:absolute;right:40px;top:120px;width:150px;height:130px;background:radial-gradient(circle at 50% 50%,#7cc04a 0%,#3f8f2b 55%,rgba(255,255,255,0) 72%)}

/* services */
.services{height:380px;position:relative}
.section-title{font-size:22px;color:var(--ink);font-weight:700}
.service-row{display:flex;gap:40px;margin-top:30px;padding:0 60px;position:relative}
.service-card{width:220px}
.service-card .thumb{height:140px}
.service-card h3{font-size:11px;font-weight:600;color:var(--ink);margin-top:14px;text-align:center}
.carousel-btn{position:absolute;top:55px;width:28px;height:36px;border:1px solid #cfd6da;background:var(--white);display:flex;align-items:center;justify-content:center}
.carousel-btn.prev{left:0}.carousel-btn.next{right:0}

/* why */
.why{background:var(--light);height:300px;padding-top:36px}
.why-grid{display:flex;justify-content:space-between;margin-top:30px;padding:0 40px}
.why-item{width:210px;text-align:center}
.why-icon{width:64px;height:64px;border-radius:50%;background:var(--teal);margin:0 auto 14px;display:flex;align-items:center;justify-content:center}
.why-item h3{font-size:13px;font-weight:700;color:var(--ink);margin-bottom:6px}
.why-item p{font-size:11px;line-height:1.5}

/* team */
.team{height:340px;padding-top:60px;position:relative}
.team h2{font-size:22px;line-height:1.3;color:var(--ink);font-weight:700;width:640px}
.team .lead{font-size:13px;margin:12px 0 10px}
.btn{display:inline-block;background:var(--teal);color:var(--white);font-size:13px;font-weight:600;padding:12px 28px;text-decoration:none;margin-top:18px}
.team-art{position:absolute;right:40px;top:80px;width:270px;height:180px;background:linear-gradient(180deg,#bfe3ea 0%,#8fcdd9 60%,#5fb4c4 100%)}

/* cta */
.cta{background:var(--teal);height:96px}
.cta .container{display:flex;align-items:center;justify-content:space-between;height:96px;padding:0 80px 0 40px}
.cta h2{color:var(--white);font-size:24px;font-weight:700}
.btn-dark{background:#1d2226;color:var(--white);font-size:13px;font-weight:600;padding:14px 32px}

/* footer */
.site-footer{background:var(--footer);height:256px;padding-top:30px;color:#b9c0c5}
.footer-grid{display:flex;gap:60px;padding:0 10px}
.footer-col h4{color:var(--white);font-size:15px;font-weight:700;margin-bottom:16px}
.news{width:220px}
.news-item{display:flex;gap:12px;margin-bottom:14px}
.news-thumb{width:58px;height:46px;background:linear-gradient(135deg,#5e6a72,#39434a);flex:none}
.news-item b{display:block;color:var(--white);font-size:11px;margin-bottom:3px}
.news-item span{font-size:10px;line-height:1.4}
.links{width:250px;display:flex;flex-wrap:wrap}
.links h4{width:100%}
.links ul{list-style:none;width:50%}
.links li{font-size:11px;line-height:2.1}
.newsletter{width:200px}
.field{height:30px;border:1px solid #4a5258;margin-bottom:8px;font-size:10px;line-height:28px;padding-left:10px;color:#8c959b}
.subscribe{background:var(--teal);color:var(--white);font-size:11px;height:30px;line-height:30px;text-align:center;font-weight:600}
.contact{width:230px;font-size:11px;line-height:1.5}
.contact p{display:flex;gap:10px;margin-bottom:8px}
.contact .dot{width:14px;height:14px;background:var(--teal);border-radius:50%;flex:none;margin-top:2px}
.social{display:flex;gap:6px;margin-top:6px}
.social span{width:22px;height:22px;background:#3d454b}
.bottom-bar{position:absolute;left:0;right:0;bottom:0;height:36px;background:var(--footer-deep);font-size:10px;color:#8c959b}
.bottom-bar .container{line-height:36px;display:flex;justify-content:space-between}
</style>
</head>
<body>

<header class="site-header">
  <div class="brand"><span class="brand-mark"></span><span class="brand-name">Harbor Broker Ledger &amp; Payroll Services</span></div>
  <p class="tagline">Specialists in providing accounting support services to Independent Insurance Agencies</p>
  <nav class="main-nav">
    <a class="active" href="#">HOME</a><a href="#">ABOUT US</a><a href="#">COMPANY</a><a href="#">OUR SERVICES</a><a href="#">HOW IT WORKS</a><a href="#">RESOURCES</a><a href="#">CONTACT US</a><a href="#">BLOG</a>
  </nav>
</header>

<section class="hero">
  <div class="hero-photo" role="img" aria-label="Photo of business colleagues reviewing documents at a desk"></div>
  <p class="hero-caption">HBLP is a professional Accounting / Bookkeeping firm located in Connecticut dedicated exclusively to Independent Insurance Agencies.</p>
  <div class="hero-arrows">
    <span><svg width="12" height="12" viewBox="0 0 12 12"><path d="M8 1L3 6l5 5" stroke="#fff" stroke-width="2" fill="none"/></svg></span>
    <span><svg width="12" height="12" viewBox="0 0 12 12"><path d="M4 1l5 5-5 5" stroke="#fff" stroke-width="2" fill="none"/></svg></span>
  </div>
</section>

<section class="need-help container">
  <h2>Need help with your insurance agency's accounting and bookkeeping?</h2>
  <ul class="tick-list">
    <li>The same team of insurance agency bookkeeping professionals for over 20 years</li>
    <li>Have a core team based locally in a centralized office environment in Connecticut for your service</li>
    <li>Be associated with a skilled financial team experienced in agency management systems and reporting</li>
  </ul>
  <div class="money-art" role="img" aria-label="Illustration of a dollar sign with a rising arrow"></div>
</section>

<section class="services container">
  <h2 class="section-title">Our Services</h2>
  <div class="service-row">
    <span class="carousel-btn prev"><svg width="10" height="12" viewBox="0 0 10 12"><path d="M7 1L2 6l5 5" stroke="#8a959c" stroke-width="2" fill="none"/></svg></span>
    <div class="service-card"><div class="thumb" role="img" aria-label="Photo of financial paperwork and a calculator" style="background:linear-gradient(135deg,#d9dde0,#9aa5ad)"></div><h3>Record Direct Bill Commissions</h3></div>
    <div class="service-card"><div class="thumb" role="img" aria-label="Illustration of accounting tasks on an orange background" style="background:linear-gradient(135deg,#f7b733,#f28c1c)"></div><h3>Reconcile &amp; Pay Agency Bill Premiums</h3></div>
    <div class="service-card"><div class="thumb" role="img" aria-label="Illustration of figures climbing a rising chart" style="background:linear-gradient(135deg,#f4f4f4,#d7dcdf)"></div><h3>Reconcile General Ledger Accounts</h3></div>
    <div class="service-card"><div class="thumb" role="img" aria-label="Illustration of a magnifying glass over financial charts" style="background:linear-gradient(135deg,#eef1f3,#bcc6cc)"></div><h3>Prepare &amp; Interpret Financial Statements</h3></div>
    <span class="carousel-btn next"><svg width="10" height="12" viewBox="0 0 10 12"><path d="M3 1l5 5-5 5" stroke="#8a959c" stroke-width="2" fill="none"/></svg></span>
  </div>
</section>

<section class="why">
  <div class="container">
    <h2 class="section-title">Why It Works</h2>
    <div class="why-grid">
      <div class="why-item">
        <div class="why-icon"><svg width="28" height="28" viewBox="0 0 28 28"><path d="M6 22l2-6L19 5l4 4-11 11z" fill="#fff"/></svg></div>
        <h3>Educated &amp; Trained Staff</h3>
        <p>All our staff are degreed and fully trained on agency systems before starting.</p>
      </div>
      <div class="why-item">
        <div class="why-icon"><svg width="28" height="28" viewBox="0 0 28 28"><path d="M14 3l3.3 7 7.2.8-5.4 5 1.5 7.2L14 19.4 7.4 23l1.5-7.2-5.4-5 7.2-.8z" fill="#fff"/></svg></div>
        <h3>Quality Control</h3>
        <p>Financial statements are reviewed by experienced CPAs and reconciled monthly.</p>
      </div>
      <div class="why-item">
        <div class="why-icon"><svg width="28" height="28" viewBox="0 0 28 28"><path d="M3 13L25 4l-6 20-5-7z" fill="#fff"/></svg></div>
        <h3>Separation of Duties</h3>
        <p>A full accounting department provides a system of checks and balances.</p>
      </div>
      <div class="why-item">
        <div class="why-icon"><svg width="28" height="28" viewBox="0 0 28 28"><path d="M14 3l9 4v6c0 6-4 10-9 12-5-2-9-6-9-12V7z" fill="#fff"/></svg></div>
        <h3>Data Security</h3>
        <p>All computer equipment is secured and monitored by staff and outside firms.</p>
      </div>
    </div>
  </div>
</section>

<section class="team container">
  <h2>Experienced team of insurance agency bookkeeping professionals maintaining your books</h2>
  <p class="lead">Affordable, professional services for less than the cost of an in-house bookkeeper</p>
  <ul class="tick-list">
    <li>Pay for what you need, when you need it</li>
    <li>No more year end headaches – eliminate the need for a temp</li>
    <li>Ongoing updates of financial records and reports</li>
  </ul>
  <a class="btn" href="#">Read More</a>
  <div class="team-art" role="img" aria-label="Illustration of business figures around a large dollar sign"></div>
</section>

<section class="cta">
  <div class="container">
    <h2>Need Help with LedgerDesk or BrokerSuite Accounting?</h2>
    <span class="btn-dark">Click Here</span>
  </div>
</section>

<footer class="site-footer">
  <div class="container footer-grid">
    <div class="footer-col news">
      <h4>News</h4>
      <div class="news-item"><div class="news-thumb" role="img" aria-label="News thumbnail photo"></div><div><b>Year end closing tips</b><span>Get your agency books ready early this season.</span></div></div>
      <div class="news-item"><div class="news-thumb" role="img" aria-label="News thumbnail photo"></div><div><b>New payroll rules</b><span>What agency owners should know this quarter.</span></div></div>
    </div>
    <div class="footer-col links">
      <h4>Quick Links</h4>
      <ul><li>Home</li><li>About Us</li><li>Our Services</li><li>Blog</li></ul>
      <ul><li>Testimonials</li><li>Privacy Policy</li><li>Sitemap</li><li>Terms &amp; Conditions</li></ul>
    </div>
    <div class="footer-col newsletter">
      <h4>Newsletter</h4>
      <div class="field">Your Name</div>
      <div class="field">Email Address</div>
      <div class="subscribe">Subscribe</div>
    </div>
    <div class="footer-col contact">
      <h4>Contact</h4>
      <p><span class="dot"></span><span>Harbor Broker Ledger &amp; Payroll Services<br>214 Quayside Road, Mystic Harbor, CT 06355</span></p>
      <p><span class="dot"></span><span>hello@harborbrokerledgers.com</span></p>
      <p><span class="dot"></span><span>(860) 555-0148</span></p>
      <div class="social"><span></span><span></span><span></span><span></span></div>
    </div>
  </div>
  <div class="bottom-bar"><div class="container"><span>© 2024 Harbor Broker Ledger &amp; Payroll Services. All rights reserved.</span><span>www.harborbrokerledgers.com</span></div></div>
</footer>

</body>
</html>
```